Valu Tea Label & packaging for a premium tea brand. For local and global market

Create a look and feel for a box and rectangle tin. We are looking for a luxe packaging design for a new tea brand based in Kenya called 'Valu Tea'. Kenya is home to the finest teas in the world and Valu tea looks to embody that fact. Valu Tea uses the most premium of Kenyan Tea, Black tea, Purple tea, White Tea, Green tea, Hibiscus Tea and Moringa Tea. Valu Tea is handpicked from Kenya's highlands. This project will include the look and feel of the different teas described above. The copy on the main face of the box should read 'Premium Kenyan Tea' The box will contain 25 tagged tea bags, with a net weight of 50 gms.

On one side of the box will read 'packaging instructions' To fully savour this Valu premium tea, use one tea bag for each cup, add some freshly bolded water and wait for 2 minutes as you enjoy the sweet aroma of our tea, stir and serve' Ingredients : Black Tea, and for the others the same : Hibiscus Tea, Green Tea, Purple Tea, White tea. should also feature on the label: Produce of Kenya.

Target Market(s)

Premium

Industry/Entity Type

Agribusiness

Font styles to use
Script

Colors

Designer to choose colors to be used in the design.

Requirements
Must have
• Luxe look and feel
Nice to have
• I have attached the Valu tea logo and images of brands I'd lile the designer to be inspired by.
Should not have
• Green and yellow colours

```html
<!DOCTYPE html>
<html lang="en">
<head>
<meta charset="utf-8">
<title>Valu Tea – Premium Kenyan Tea packaging</title>
<link rel="stylesheet" href="https://fonts.googleapis.com/css2?family=Great+Vibes&family=Playfair+Display:ital,wght@1,600&display=swap">
<style>
  :root {
    --canvas: #ffffff;
    --frame: #3b3b3b;
    --panel: #fbfbfb;
    --ornament-dark: #2c2c2c;
    --ornament-light: #6a6a6a;
    --window-ring: #8e8e8e;
    --ink: #111111;
    --window-text: #f4f4f4;
    --accent-red: #f40d0d;
    --accent-pink: #ff0aa6;
  }
  html, body {
    margin: 0;
    width: 1200px;
    height: 1200px;
    overflow: hidden;
    background: var(--canvas);
  }
  .stage {
    position: relative;
    width: 1200px;
    height: 1200px;
  }
  .tea-box {
    position: absolute;
    top: 301px;
    width: 492px;
    height: 615px;
    overflow: visible;
  }
  .tea-box--black { left: 43px; --accent: var(--accent-red); }
  .tea-box--purple { left: 663px; --accent: var(--accent-pink); }

  .box-frame { fill: var(--frame); }
  .front-panel { fill: var(--panel); }
  .window-ring { fill: none; stroke: var(--window-ring); stroke-width: 4; }
  .brand-dot { fill: var(--accent); }
  .ribbon { fill: var(--accent); }
  .brand-name {
    font-family: "Great Vibes", cursive;
    font-size: 64px;
    fill: var(--window-text);
  }
  .product-title {
    font-family: "Great Vibes", cursive;
    font-size: 44px;
    fill: var(--ink);
  }
  .variety, .bag-count {
    font-family: "Great Vibes", cursive;
    fill: var(--ink);
  }
  .variety { font-size: 34px; }
  .bag-count { font-size: 29px; }
  .net-weight {
    font-family: "Playfair Display", serif;
    font-style: italic;
    font-weight: 600;
    font-size: 15px;
    fill: var(--ink);
  }
</style>
</head>
<body>
<main class="stage">

  <svg class="tea-box tea-box--black" viewBox="0 0 492 615" aria-label="Valu Tea black tea box front">
    <defs>
      <linearGradient id="ornament-black" x1="0" y1="0" x2="1" y2="0.4">
        <stop offset="0" stop-color="var(--ornament-dark)"/>
        <stop offset="0.6" stop-color="#4a4a4a"/>
        <stop offset="1" stop-color="var(--ornament-light)"/>
      </linearGradient>
      <radialGradient id="leaves-black" cx="0.5" cy="0.5" r="0.5">
        <stop offset="0" stop-color="#3a2a1c"/>
        <stop offset="1" stop-color="#141210"/>
      </radialGradient>
    </defs>
    <rect class="box-frame" x="0" y="0" width="492" height="615"/>
    <rect x="0" y="0" width="492" height="237" fill="url(#ornament-black)" role="img" aria-label="silver floral scroll ornament on charcoal"/>
    <rect class="front-panel" x="23" y="237" width="448" height="356"/>
    <circle cx="243" cy="237" r="132" fill="url(#leaves-black)" role="img" aria-label="window showing loose black tea leaves"/>
    <circle class="window-ring" cx="243" cy="237" r="132"/>
    <circle class="brand-dot" cx="180" cy="232" r="9"/>
    <text class="brand-name" x="252" y="256" text-anchor="middle">Valu</text>
    <text class="product-title" x="246" y="467" text-anchor="middle">Premium Kenyan Tea</text>
    <polygon class="ribbon" points="-2,508 -2,522 181,519 181,518"/>
    <polygon class="ribbon" points="494,508 494,522 305,519 305,518"/>
    <text class="variety" x="246" y="527" text-anchor="middle">Black tea</text>
    <text class="bag-count" x="244" y="563" text-anchor="middle">25 tagged tea bags</text>
    <text class="net-weight" x="463" y="586" text-anchor="end">net weight 50 gm</text>
  </svg>

  <svg class="tea-box tea-box--purple" viewBox="0 0 492 615" aria-label="Valu Tea purple tea box front">
    <defs>
      <linearGradient id="ornament-purple" x1="0" y1="0" x2="1" y2="0.4">
        <stop offset="0" stop-color="var(--ornament-dark)"/>
        <stop offset="0.6" stop-color="#4a4a4a"/>
        <stop offset="1" stop-color="var(--ornament-light)"/>
      </linearGradient>
      <radialGradient id="leaves-purple" cx="0.5" cy="0.5" r="0.5">
        <stop offset="0" stop-color="#3c1a2a"/>
        <stop offset="1" stop-color="#141012"/>
      </radialGradient>
    </defs>
    <rect class="box-frame" x="0" y="0" width="492" height="615"/>
    <rect x="0" y="0" width="492" height="237" fill="url(#ornament-purple)" role="img" aria-label="silver floral scroll ornament on charcoal"/>
    <rect class="front-panel" x="23" y="237" width="448" height="356"/>
    <circle cx="243" cy="237" r="132" fill="url(#leaves-purple)" role="img" aria-label="window showing loose purple tea leaves"/>
    <circle class="window-ring" cx="243" cy="237" r="132"/>
    <circle class="brand-dot" cx="180" cy="232" r="9"/>
    <text class="brand-name" x="252" y="256" text-anchor="middle">Valu</text>
    <text class="product-title" x="246" y="467" text-anchor="middle">Premium Kenyan Tea</text>
    <polygon class="ribbon" points="-2,508 -2,522 181,519 181,518"/>
    <polygon class="ribbon" points="494,508 494,522 305,519 305,518"/>
    <text class="variety" x="246" y="527" text-anchor="middle">Black tea</text>
    <text class="bag-count" x="244" y="563" text-anchor="middle">25 tagged tea bags</text>
    <text class="net-weight" x="463" y="586" text-anchor="end">net weight 50 gm</text>
  </svg>

</main>
</body>
</html>
```